Print design needed to improve the layout and look of some existing documents

We need someone to take a couple of existing documents that we have and make them look much better using our existing logo and corporate colors etc. We require these to be delivered in a format that will allow our staff to edit the content as necessary via Microsoft word for conversion once finalized into a PDF. Ideally, we will also be able to use this as a newsletter template or for other documents that might be required in our business. www.calderfinch.com.au
Updates

Project Deadline Extended Reason: So far, I have only seen one design that I believe is quite good quality. Added Sunday, July 3, 2016

Target Market(s)

Business owners, executives, retirees

Industry/Entity Type

Financial Service

Font styles to use
Serif

Requirements
Must have
• Design that uses our existing branding and colors. It also needs to be ina form that we can edit the content / update easily. Ideally the format / layout could also be used for other documents such as short newsletters etc.
Nice to have
• Fresh, simple and crisp. Very professional looking.
Should not have
• strange fonts, weird layouts.

```html
<!DOCTYPE html>
<html lang="en">
<head>
<meta charset="utf-8">
<title>Calder Finch – Financial Services Guide, pages 4–5</title>
<link rel="stylesheet" href="https://fonts.googleapis.com/css2?family=Open+Sans:wght@400;600;700&display=swap">
<style>
  :root{
    --bg:#e6e6e6;
    --paper:#ffffff;
    --panel:#f4f4f4;
    --blue:#0f98d6;
    --green:#5db233;
    --text:#4a4a4a;
    --brand-grey:#5a5a5a;
  }
  *{box-sizing:border-box;margin:0;padding:0}
  html,body{width:1200px;height:793px;overflow:hidden}
  body{background:var(--bg);font-family:"Open Sans",Arial,sans-serif;color:var(--text)}
  .page{position:absolute;top:28px;width:524px;height:736px;background:var(--paper);padding:16px}
  .page--left{left:60px}
  .page--right{left:616px}
  .panel{position:relative;width:100%;height:100%;background:var(--panel)}
  .brand{position:absolute;top:26px;left:20px;display:flex;align-items:center;gap:8px}
  .brand__dot{width:18px;height:18px;border-radius:50%;background:var(--blue)}
  .brand__name{font-size:17px;font-weight:400;letter-spacing:1.5px;color:var(--brand-grey)}
  .col{position:absolute;width:212px;font-size:8.4px;line-height:11.5px}
  .col--a{left:19px}
  .col--b{left:256px}
  .col p{margin:0 0 11.5px}
  .section-title{display:flex;align-items:flex-start;gap:5px;color:var(--blue);font-size:12.8px;font-weight:600;line-height:15.5px;margin:0 0 14px}
  .section-title svg{flex:0 0 14px;margin-top:1px}
  .subhead{color:var(--blue);font-size:8.6px;font-weight:600;margin:0 0 8px}
  .gap{height:16px}
  .bullets{list-style:none;margin:0 0 14px}
  .bullets li{position:relative;padding-left:12px;margin-bottom:5px}
  .bullets li::before{content:"";position:absolute;left:1px;top:4.5px;width:3.5px;height:3.5px;border-radius:50%;background:var(--blue)}
  .bullets--loose li{line-height:15px;margin-bottom:0}
  .footer{position:absolute;left:0;right:0;bottom:0;height:22px;background:var(--blue);color:#fff;font-size:6.6px;display:flex;align-items:center;padding-left:19px}
  .footer__page{position:absolute;right:0;top:0;width:46px;height:22px;background:var(--green);font-size:11px;font-weight:700;display:flex;align-items:center;justify-content:center}
  .footer__sep{margin:0 4px}
  .footer__link{display:inline-flex;align-items:center;gap:3px;margin-left:8px}
</style>
</head>
<body>

<svg width="0" height="0" style="position:absolute">
  <defs>
    <symbol id="icon-arrow" viewBox="0 0 14 14">
      <circle cx="7" cy="7" r="6" fill="none" stroke="#5db233" stroke-width="1.3"/>
      <path d="M5.8 4.3 L8.5 7 L5.8 9.7" fill="none" stroke="#5db233" stroke-width="1.4" stroke-linecap="round" stroke-linejoin="round"/>
    </symbol>
    <symbol id="icon-link" viewBox="0 0 10 10">
      <path d="M4 6 L6 4 M3.2 4.6 L2 5.8 a1.6 1.6 0 0 0 2.2 2.2 L5.4 6.8 M4.6 3.2 L5.8 2 a1.6 1.6 0 0 1 2.2 2.2 L6.8 5.4" fill="none" stroke="#fff" stroke-width="0.9" stroke-linecap="round"/>
    </symbol>
  </defs>
</svg>

<section class="page page--left">
  <div class="panel">
    <div class="brand"><span class="brand__dot"></span><span class="brand__name">CALDER FINCH</span></div>

    <div class="col col--a" style="top:80px">
      <h2 class="section-title"><svg width="14" height="14"><use href="#icon-arrow"/></svg>Commissions</h2>
      <p>The Harlow Trust, Neil Ashworth, Martin Okafor and Daniel Pryce may receive commissions and other benefits from some product and service providers.</p>
      <p>The commission amount will vary depending on the product or service which is recommended. We will disclose the exact amount in the SoA or RoA.</p>
      <div class="gap" style="height:4px"></div>
      <h3 class="subhead">Insurance Commissions</h3>
      <p>We may receive a one-off upfront commission when you take out an insurance policy we recommend.</p>
      <p>We may also receive a monthly commission payment for as long as you continue to hold the policy.</p>
      <div class="gap" style="height:4px"></div>
      <h3 class="subhead">Placement Commissions</h3>
      <p>We may receive a placement commission on capital raisings undertaken by companies. This includes initial public offerings and rights issues. These are one-off payments.</p>
      <div class="gap" style="height:4px"></div>
      <h3 class="subhead">Other Benefits</h3>
      <p>We may receive additional benefits by way of sponsorship of education seminars, conferences or training days. Details of any benefits received above $100 will be maintained on a register which is available to you on request.</p>
      <div class="gap" style="height:20px"></div>
      <h2 class="section-title" style="margin-bottom:10px"><svg width="14" height="14"><use href="#icon-arrow"/></svg>Referral Fees and Commissions</h2>
      <p>In some situations we may receive fees or commissions when we refer you to external parties. We will disclose the referral arrangements to you whenever we refer you to an external party.</p>
      <p>In some situations we may pay fees or commissions to external parties who have referred you to us. We will disclose the referral arrangements to you when we provide you with a SoA.</p>
    </div>

    <div class="col col--b" style="top:74px">
      <h2 class="section-title"><svg width="14" height="14"><use href="#icon-arrow"/></svg>Conflicts of Interest</h2>
      <h3 class="subhead">We may hold investments we recommend</h3>
      <p>Neil Ashworth, Martin Okafor and Daniel Pryce may provide advice on investments which they hold or may hold in their own personal portfolios.</p>
      <p>We will disclose the size and nature of these holdings where there may be a conflict of interest with the advice that we provide.</p>
      <div class="gap" style="height:16px"></div>
      <h2 class="section-title" style="margin-bottom:20px"><svg width="14" height="14"><use href="#icon-arrow"/></svg>Making a Complaint</h2>
      <p>We will endeavour to provide you with the best advice and service at all times.</p>
      <p>If for any reason you are not satisfied with our services we encourage you to contact us and to put your complaint in writing.</p>
      <p>If you are not satisfied with our response you can refer it to the Financial Ombudsman Service (FOS). You can contact FOS on 1300 555 014.</p>
      <p>This service is available to you free of charge.</p>
      <div class="gap" style="height:4px"></div>
      <h2 class="section-title" style="margin-bottom:20px"><svg width="14" height="14"><use href="#icon-arrow"/></svg>Your Privacy</h2>
      <p>Calder Finch Wealth is committed to protecting your privacy. We have a Privacy Policy which sets out how we collect, hold, use and disclose your personal information.</p>
      <p>We will collect personal information from you so that we can understand your personal situation and provide you with advice which meets your needs and objectives.</p>
      <p>We will also collect information from you to meet our obligations under the Anti-Money Laundering and Counter-Terrorism Financing Act.</p>
      <p>We will generally collect this information directly from you. However in some cases we will seek your</p>
    </div>

    <footer class="footer">
      Calder Finch Wealth Pty Ltd<span class="footer__sep">•</span>AFSL 470312<span class="footer__sep">•</span>ABN 51 612 309 774
      <span class="footer__link"><svg width="8" height="8"><use href="#icon-link"/></svg>www.calderfinch.com.au</span>
      <span class="footer__page">4</span>
    </footer>
  </div>
</section>

<section class="page page--right">
  <div class="panel">
    <div class="brand"><span class="brand__dot"></span><span class="brand__name">CALDER FINCH</span></div>

    <div class="col col--a" style="top:66px">
      <p>authority to collect if from other parties such as your accountant or your superannuation fund.</p>
      <p>If you do not provide us with all of the information that we request, we may not be able to provide our services to you.</p>
      <p>We will hold and use your personal information so that we can continue to provide our services to you. We will only disclose your personal information to external parties where:</p>
      <ul class="bullets bullets--loose">
        <li>The law requires us to do so</li>
        <li>You consent for us to do so</li>
        <li>You direct us to provide information to other professional services providers such as your Accountant or Lawyer.</li>
      </ul>
      <div class="gap" style="height:8px"></div>
      <p>Our Privacy Policy contains further information on how we collect, hold, use and disclose your personal information. It also sets out how you can access the information we hold about you, how to have it corrected and how to complain where you are not satisfied with how we have handled your personal information.</p>
      <p>Our full Privacy Policy is available on our website.</p>
      <div class="gap" style="height:2px"></div>
      <h2 class="section-title" style="margin-bottom:10px"><svg width="14" height="14"><use href="#icon-arrow"/></svg>Managed Discretionary Account Service</h2>
      <p>Calder Finch Wealth is authorised by ASIC to provide a Managed Discretionary Account (MDA) service.</p>
      <p>An MDA Service means we will manage your investments and undertake transactions without obtaining your approval before each transaction. An MDA service enables us to quickly and efficiently make changes to your investments.</p>
      <p>We offer an MDA service which is restricted to investments held on a regulated platform (for example the Harbourline Private Wrap).</p>
      <p>The MDA service only allows us to make changes to the investments within your account. It does not give us authority to withdraw funds from the</p>
    </div>

    <div class="col col--b" style="top:66px">
      <p>account, to make additional contributions to the account or to transact on any of your investments held outside the account.</p>
      <h3 class="subhead">MDA Service Agreement &amp; Investment Program</h3>
      <p>We will provide you with a SoA and service agreements where we recommend you enter an MDA service. The SoA will explain why we believe the service is in your best interests and why it is suitable for you.</p>
      <p>The SoA and agreement will comply with Division 3 of Part 7.7 of the Corporations Act. It will also set out the terms and conditions of the MDA service and the Investment Program including:</p>
      <ul class="bullets" style="line-height:13px">
        <li>The nature and scope of our discretion under the service including any discretion we must exercise</li>
        <li>The investment strategy that is to be applied in exercising the discretion</li>
        <li>An explanation of any significant risks associated with the service</li>
        <li>A warning that the MDA service may not be suitable for you if you provide limited or inaccurate information relating to your personal circumstances or those circumstances change.</li>
      </ul>
      <p>You can establish the MDA service by signing the Authority to Proceed at the back of the SoA and executing the general Power of Attorney.</p>
      <h3 class="subhead">MDA Service Risk</h3>
      <p>Subject to the discretion we hold, we will make changes to the investments in your account without first contacting you or seeking your approval. You will not be able to consider each change before it is made.</p>
    </div>

    <footer class="footer">
      Calder Finch Wealth Pty Ltd<span class="footer__sep">•</span>AFSL 470312<span class="footer__sep">•</span>ABN 51 612 309 774
      <span class="footer__link"><svg width="8" height="8"><use href="#icon-link"/></svg>www.calderfinch.com.au</span>
      <span class="footer__page">5</span>
    </footer>
  </div>
</section>

</body>
</html>
```